Label Design for Cook Marsh Kimchi Sauce – Modern Korean Fermentation Brand

We are developing the primary packaging identity for COOK MARSH, beginning with our flagship Korean Kimchi Sauce.
Cook Marsh is a contemporary Korean food brand built around an idea that is central to Korean cuisine: Tradition refined through modern food science. Our kimchi sauce is not intended to be simply another spicy Korean condiment, but rooted in authentic Korean kimchi fermentation and combines traditional fermentation knowledge with modern process control to create a consistent, flavorful and convenient shelf-stable sauce.
The goal of this project is to create a distinctive, typography-led master label and visual identity that can eventually expand across an entire Cook Marsh product family. The winning design should feel credible as the beginning of a serious international food brand, rather than as a one-off sauce label.
This first project is for our Kimchi Sauce bottle and Kimchi Paste package, but the design should establish a master brand system that can later expand into additional products such as Korean Kimchi Sauce and Korean Kimchi Paste.
Primary sauce bottle is approximately:
300 mL / 10.1 FL OZ
The label design should be developed specifically with the proportions, readability and shelf presence of a 300 mL sauce bottle in mind.
We want the design to place much greater emphasis on text, font, typography and brand hierarchy than on graphics or illustration. Should be driven primarily by distinctive typography, strong font selection or custom lettering, clear hierarchy, strong use of scale and proportion, memorable wordmark treatment, spacing and composition, recognizable label structure, with Cook Marsh and Kimchi Sauce as the visual focus. Graphics and illustrations can be used, but they should be secondary and restrained, not the main feature of the package.
A brand such as Verluna, particularly its 300 mL bottle presentation, is useful as a general reference for the importance of typography, simplicity, hierarchy, shelf recognition and longevity. We are not looking to copy Verluna's design, but we appreciate how strongly the brand is communicated through text and label structure rather than decorative graphics.
The brand concept combines:
• Korean fermentation heritage
• modern scientific precision
• real food / plant-forward ingredients
• global culinary versatility
Front Label Priorities
The front label should clearly communicate:
1. COOK MARSH as the master brand
2. KIMCHI SAUCE as the product
3. 300 mL / 10.1 FL OZ
4. A premium, clean and modern aesthetic
5. An appetizing and confident Korean identity
Possible supporting themes or optional secondary messaging:
• Authentically Fermented
• Crafted for Consistency
• Korean Chili Blend
• Bold & Tangy
• Tradition Refined by Science
These are secondary messages only. We prefer strong typography and hierarchy over excessive front-label copy. We are open to creative exploration, but the design should feel typography-led, modern, premium, bold, clean, warm, appetizing, rooted in Korean heritage, recognizable from a distance, scalable across future products
Please keep graphics minimal and secondary.
Ingredient illustrations such as cabbage, chili peppers, garlic or herbs may be used if they support the design, but they should not dominate the label.
Our preliminary concepts use more ingredient illustration than we ultimately want. We are sharing them as a starting point, but we would like designers to move the brand toward a cleaner, stronger and more typography-focused identity.
A strong concept should still work even if most decorative graphics were removed.
Please avoid:
• illustration-heavy labels
• overly busy ingredient graphics
• overly rustic packaging
• typography that feels generic or secondary
• copycat designs of existing trendy sauce brands
The final design should make the consumer remember COOK MARSH, not simply the pictures on the bottle.

```html
<!DOCTYPE html>
<html lang="en">
<head>
<meta charset="utf-8">
<title>Cook Marsh Kimchi Sauce – Front Label</title>
<link rel="stylesheet" href="https://fonts.googleapis.com/css2?family=Paytone+One&family=Open+Sans:wght@600;700;800&family=Noto+Sans+KR:wght@500&display=swap">
<style>
  :root {
    --chili: #a61e22;
    --chili-soft: #b23a2f;
    --chili-deep: #7c1417;
    --cream: #f8efe2;
    --ink: #1d1d1d;
    --paper: #ffffff;
    --stage: #ece8e2;
  }
  html, body {
    margin: 0;
    width: 1200px;
    height: 853px;
    overflow: hidden;
    background: var(--stage);
  }
  .canvas {
    width: 1200px;
    height: 853px;
    display: flex;
    align-items: center;
    justify-content: center;
  }
  .label {
    display: block;
    width: 698px;
    height: 853px;
    background: var(--paper);
  }
  .brand-top { font-family: "Open Sans", sans-serif; font-weight: 600; fill: var(--ink); letter-spacing: 7px; }
  .brand-main { font-family: "Open Sans", sans-serif; font-weight: 800; fill: var(--ink); letter-spacing: 3px; }
  .wordmark {
    font-family: "Paytone One", sans-serif;
    fill: var(--chili);
    stroke: var(--paper);
    stroke-width: 8px;
    paint-order: stroke;
    stroke-linejoin: round;
  }
  .wordmark-shadow { font-family: "Paytone One", sans-serif; fill: var(--chili-deep); }
  .kicker { font-family: "Open Sans", sans-serif; font-weight: 700; fill: var(--ink); letter-spacing: 2.4px; }
  .claim { font-family: "Open Sans", sans-serif; font-weight: 800; fill: var(--chili); }
  .tagline { font-family: "Open Sans", sans-serif; font-weight: 700; fill: var(--chili-soft); letter-spacing: 2px; }
  .band-text { font-family: "Open Sans", sans-serif; font-weight: 600; fill: var(--cream); }
  .hangul { font-family: "Noto Sans KR", sans-serif; font-weight: 500; fill: var(--cream); letter-spacing: 4px; }
  .volume { font-family: "Open Sans", sans-serif; font-weight: 600; fill: var(--paper); }
</style>
</head>
<body>
<main class="canvas">
  <svg class="label" viewBox="0 0 737 900" xmlns="http://www.w3.org/2000/svg" aria-label="Cook Marsh Kimchi Sauce front label">
    <!-- scalloped badge -->
    <g class="badge-outer" fill="var(--chili-soft)">
      <circle cx="372" cy="405" r="285"/>
      <circle cx="372" cy="140" r="80"/>
      <circle cx="372" cy="670" r="85"/>
      <circle cx="560" cy="215" r="95"/>
      <circle cx="185" cy="215" r="95"/>
      <circle cx="110" cy="405" r="90"/>
      <circle cx="635" cy="405" r="90"/>
      <circle cx="185" cy="600" r="95"/>
      <circle cx="560" cy="600" r="95"/>
    </g>
    <g class="badge-inner" fill="var(--cream)" stroke="var(--paper)" stroke-width="5">
      <rect x="62" y="160" width="620" height="470" rx="130"/>
      <circle cx="372" cy="150" r="80"/>
      <circle cx="372" cy="655" r="92"/>
    </g>
    <g fill="var(--cream)">
      <rect x="66" y="165" width="612" height="460" rx="126"/>
      <circle cx="372" cy="150" r="77"/>
      <circle cx="372" cy="655" r="89"/>
    </g>

    <!-- brand -->
    <rect x="360" y="108" width="24" height="24" fill="var(--chili)"/>
    <text class="brand-top" x="375" y="176" font-size="17" text-anchor="middle">COOK</text>
    <text class="brand-main" x="373" y="202" font-size="25" text-anchor="middle">MARSH</text>

    <!-- product wordmark -->
    <text class="wordmark-shadow" x="383" y="362" font-size="168" text-anchor="middle" textLength="560" lengthAdjust="spacingAndGlyphs">KIMCHI</text>
    <text class="wordmark" x="375" y="354" font-size="168" text-anchor="middle" textLength="560" lengthAdjust="spacingAndGlyphs">KIMCHI</text>
    <text class="wordmark-shadow" x="390" y="460" font-size="130" text-anchor="middle" textLength="420" lengthAdjust="spacingAndGlyphs">SAUCE</text>
    <text class="wordmark" x="382" y="452" font-size="130" text-anchor="middle" textLength="420" lengthAdjust="spacingAndGlyphs">SAUCE</text>
    <rect class="brush-stroke" x="155" y="470" width="440" height="24" rx="10" fill="var(--chili)" role="img" aria-label="Painted brush stroke underline"/>

    <text class="kicker" x="373" y="525" font-size="12" text-anchor="middle">KOREAN FERMENTATION EXPERTISE</text>

    <!-- claims -->
    <g class="claim-plant">
      <circle cx="145" cy="577" r="33" fill="var(--chili)"/>
      <path d="M145 594 C128 590 122 574 126 562 C138 564 146 574 145 594 Z M145 594 C162 590 168 574 164 562 C152 564 144 574 145 594 Z" fill="var(--cream)"/>
      <text class="claim" x="194" y="572" font-size="14">PLANT-</text>
      <text class="claim" x="194" y="590" font-size="14">BASED</text>
    </g>
    <g class="claim-postbiotic">
      <circle cx="307" cy="577" r="32" fill="none" stroke="var(--chili)" stroke-width="2.5"/>
      <g fill="var(--chili)">
        <ellipse cx="295" cy="566" rx="8" ry="11"/>
        <ellipse cx="318" cy="565" rx="7" ry="9"/>
        <ellipse cx="305" cy="588" rx="9" ry="7"/>
        <ellipse cx="322" cy="585" rx="5" ry="7"/>
        <circle cx="290" cy="586" r="4"/>
      </g>
      <text class="claim" x="350" y="581" font-size="14">POSTBIOTIC</text>
    </g>
    <g class="claim-fermented">
      <circle cx="480" cy="577" r="32" fill="none" stroke="var(--chili)" stroke-width="1.5"/>
      <g fill="var(--chili)">
        <circle cx="472" cy="566" r="7"/>
        <circle cx="490" cy="570" r="8"/>
        <circle cx="478" cy="586" r="7"/>
        <circle cx="494" cy="588" r="4"/>
        <circle cx="463" cy="580" r="3"/>
        <circle cx="486" cy="555" r="3"/>
      </g>
      <text class="claim" x="520" y="573" font-size="14">AUTHENTICALLY</text>
      <text class="claim" x="520" y="588" font-size="14">FERMENTED</text>
    </g>

    <text class="tagline" x="370" y="688" font-size="13" text-anchor="middle">TRADITION REFINED</text>
    <text class="tagline" x="372" y="704" font-size="13" text-anchor="middle">BY SCIENCE</text>

    <!-- lower band -->
    <rect x="0" y="760" width="737" height="82" fill="var(--chili-soft)"/>
    <path class="chili-icon" d="M135 812 C160 812 172 796 176 782 C180 780 184 783 182 788 C178 806 160 818 135 812 Z" fill="var(--cream)" role="img" aria-label="Chili pepper icon"/>
    <text class="band-text" x="191" y="797" font-size="12">KOREAN</text>
    <text class="band-text" x="191" y="812" font-size="12">CHILI BLEND</text>
    <line x1="278" y1="780" x2="278" y2="822" stroke="var(--cream)" stroke-opacity=".35"/>
    <text class="hangul" x="370" y="802" font-size="26" text-anchor="middle">김치 소스</text>
    <text class="band-text" x="369" y="821" font-size="11" text-anchor="middle">BOLD &amp; TANGY</text>
    <line x1="460" y1="780" x2="460" y2="822" stroke="var(--cream)" stroke-opacity=".35"/>
    <g class="consistency-icon" fill="var(--cream)">
      <circle cx="500" cy="800" r="18" fill="none" stroke="var(--cream)" stroke-width="1.5" stroke-dasharray="3 2"/>
      <circle cx="500" cy="800" r="3"/>
      <circle cx="490" cy="800" r="2"/><circle cx="510" cy="800" r="2"/>
      <circle cx="500" cy="790" r="2"/><circle cx="500" cy="810" r="2"/>
    </g>
    <text class="band-text" x="530" y="797" font-size="12">CRAFTED FOR</text>
    <text class="band-text" x="530" y="812" font-size="12">CONSISTENCY</text>

    <rect x="0" y="842" width="737" height="48" fill="var(--ink)"/>
    <text class="volume" x="368" y="872" font-size="19" text-anchor="middle">300 ml 10.1 FL OZ ℮</text>
  </svg>
</main>
</body>
</html>
```